Brill's Jewelers website (www.brillsjewelers-example.com)

We are in need of a web storefront for a retail Jewelry store.
www.brillsjewelers-example.com
https://www.facebook.com/Brills-Jewelers-Palm-Vista-740315928461257/

Brill's Jewelers is located in Coral Gables, Florida. The store has been family owned and operated since 1958. Their focus customers are high-income families that care about quality over the brand name. They mostly sell fashion jewelry and diamonds up to 8 carats. We are looking for a simple minimalistic site that their customers can view their inventory and purchase items online.

Competitors websites:
https://www.orvinjewelers-example.com/
http://www.pelvaro-example.com/
http://truecutjewelers-example.com/

Pages:
-Home (with message bulletin)
-Jewelry
We would be able to create the subpages ie Rings, Bracelets, Earrings, Necklaces, Estate, Watches, Men's, Children's
-Services
We would need sub pages ie Appraisals, Consignment, Repairs
-About us
-Contact

Target Market(s)

Local wealthy families

Coding

Number of Pages Required

Font styles to use
Serif

Requirements
Must have
• -An E-commerce site customers can buy jewelry online.
-An easy process internally to add new items to the site
-Colors are Black and White or Black and Gold
Nice to have
• I would like to stay away from face shots of random models in stock photos. I want the jewelry pieces as the focus, not models.

```html
<!DOCTYPE html>
<html lang="en">
<head>
<meta charset="utf-8">
<title>Brill's Jewelers — Storefront</title>
<link rel="stylesheet" href="https://fonts.googleapis.com/css2?family=Roboto:wght@400;500;700&display=swap">
<style>
  :root{
    --bg:#e6e6e6;
    --ink:#050608;
    --ink-soft:#0b0c10;
    --paper:#ffffff;
    --mist:#ececec;
    --text-light:#f4f4f4;
    --text-dim:#c9c9c9;
    --cookie:#1b1b1d;
    --stone-a:#dfe3ea;
    --stone-b:#3a3e48;
    --gold:#c9a45c;
    --rose:#d89a78;
    --enamel-a:#e85a7a;
    --enamel-b:#39b7d6;
    --enamel-c:#f2c23a;
  }
  *{box-sizing:border-box;margin:0;padding:0}
  html,body{width:1200px;height:1200px;overflow:hidden}
  body{background:var(--bg);font-family:'Roboto',Arial,sans-serif;position:relative;color:var(--ink)}
  .abs{position:absolute}

  /* desktop page */
  .page{position:absolute;left:215px;top:32px;width:580px;height:1135px;background:var(--ink);overflow:hidden;box-shadow:0 2px 10px rgba(0,0,0,.12)}
  .brand{color:var(--text-light);font-weight:700;letter-spacing:1px;line-height:1;white-space:nowrap}
  .tagline{color:var(--text-dim);font-size:4.6px;letter-spacing:.6px;white-space:nowrap}
  .site-header .brand{font-size:19px;left:0;width:580px;text-align:center;top:15px}
  .site-header .tagline{left:0;width:580px;text-align:center;top:36px}
  .util-icons{display:flex;gap:7px;align-items:center;color:var(--text-light);font-size:4px}
  .util-icons svg{display:block}
  .main-nav{top:60px;left:0;width:580px;height:10px}
  .main-nav span{position:absolute;transform:translateX(-50%);font-size:6.8px;color:var(--text-light);letter-spacing:.2px}

  .hero{top:70px;left:0;width:580px;height:273px;background:linear-gradient(180deg,var(--ink) 0%,var(--ink-soft) 100%)}
  .hero-title{left:63px;top:75px;font-size:20.5px;font-weight:700;color:#fff;line-height:32px}
  .hero-copy{left:66px;top:138px;width:200px;font-size:7.4px;color:var(--text-light);line-height:17px}
  .hero-cta{left:66px;top:213px;font-size:11px;color:#fff;display:flex;align-items:center;gap:6px}
  .hero-photo{left:300px;top:60px;width:270px;height:200px;background:radial-gradient(circle at 32% 45%,var(--stone-a) 0%,#8d93a0 18%,transparent 34%),radial-gradient(circle at 76% 52%,var(--stone-a) 0%,#7d8390 20%,transparent 36%),var(--ink);border-radius:2px}

  .arrivals{top:343px;left:0;width:580px;height:105px}
  .arrivals-label{left:63px;top:5px;font-size:6.6px;font-weight:700;color:#fff}
  .arrival-tile{top:0;height:105px;width:104px}

  .jewelry-nav{top:448px;left:0;width:580px;height:104px;background:var(--mist)}
  .jewelry-nav h2{position:absolute;left:63px;top:37px;font-size:25px;font-weight:500;color:var(--ink)}
  .jewelry-nav a{position:absolute;font-size:14px;color:var(--ink);text-decoration:none}

  .feature{top:552px;left:0;width:580px;height:326px;background:var(--paper)}
  .feature-brand{left:42px;top:28px;font-size:22px;font-weight:400;color:var(--ink)}
  .feature-line{left:58px;top:68px;font-size:12.5px;color:#333}
  .piece{border-radius:50%}

  .site-footer{top:878px;left:0;width:580px;height:226px;background:var(--ink)}
  .site-footer .brand{font-size:16px;left:70px;top:73px}
  .site-footer .tagline{left:70px;top:90px}
  .foot-col{top:70px;font-size:6.2px;color:var(--text-light);line-height:14.5px}
  .foot-col h3{font-size:6.2px;font-weight:400;margin-bottom:14px}
  .copyright{left:0;width:580px;text-align:center;top:210px;font-size:7.2px;font-weight:500;color:var(--text-light)}

  .cookie-bar{top:1104px;left:0;width:580px;height:31px;background:var(--cookie);color:var(--text-light)}
  .cookie-text{left:38px;top:7px;width:400px;font-size:4.6px;line-height:8px}
  .cookie-link{left:456px;top:12px;font-size:5px;text-decoration:underline}
  .cookie-accept{left:506px;top:8px;width:60px;height:14px;background:var(--ink);font-size:5px;display:flex;align-items:center;justify-content:center}

  /* mobile page */
  .mobile{position:absolute;left:825px;top:32px;width:160px;height:345px;background:var(--ink);overflow:hidden;box-shadow:0 2px 10px rgba(0,0,0,.12)}
  .mobile .brand{font-size:15px;left:14px;top:30px}
  .mobile .tagline{font-size:3.8px;left:14px;top:47px}
  .mobile .hero-title{left:17px;top:90px;font-size:10.6px;font-weight:400;line-height:18px}
  .mobile .hero-copy{left:20px;top:131px;width:120px;font-size:5.3px;line-height:17px}
  .mobile .hero-cta{left:20px;top:208px;font-size:10.5px}
  .mobile .hero-photo{left:14px;top:240px;width:134px;height:86px}
</style>
</head>
<body>

<main class="page" aria-label="Brill's Jewelers home page, desktop">
  <header class="site-header">
    <div class="abs brand">BRILL'S</div>
    <div class="abs tagline">YOUR HOMETOWN JEWELER</div>
    <div class="abs util-icons" style="left:502px;top:20px">
      <svg width="7" height="9" viewBox="0 0 7 9" fill="none" stroke="#fff" stroke-width="1"><circle cx="3.5" cy="2.5" r="2"/><path d="M0.5 8.5v-1a3 3 0 0 1 6 0v1z"/></svg>
      <span style="display:flex;gap:1px;align-items:center"><svg width="10" height="9" viewBox="0 0 10 9" fill="none" stroke="#fff" stroke-width="1"><path d="M5 8.2 1.2 4.5A2.2 2.2 0 0 1 5 1.9a2.2 2.2 0 0 1 3.8 2.6z"/></svg>0</span>
      <span style="display:flex;gap:1px;align-items:center"><svg width="10" height="9" viewBox="0 0 10 9" fill="none" stroke="#fff" stroke-width="1"><path d="M0.5 1h1.6l1.3 5h5l1-3.6H2.7"/><circle cx="4" cy="7.8" r=".7"/><circle cx="7.6" cy="7.8" r=".7"/></svg>0</span>
    </div>
    <nav class="abs main-nav">
      <span style="left:128px">HOME</span>
      <span style="left:206px">JEWELRY</span>
      <span style="left:288px">SERVICES</span>
      <span style="left:367px">ABOUT</span>
      <span style="left:447px">CONTACT</span>
    </nav>
  </header>

  <section class="abs hero">
    <h1 class="abs hero-title">Your Hometown Jeweler<br>Just Got a New Home</h1>
    <p class="abs hero-copy">You have trusted us for decades with your fine jewelry, custom designs, and repairs. Now come in and see what's in store!</p>
    <div class="abs hero-cta">Visit&nbsp; us today
      <svg width="8" height="7" viewBox="0 0 8 7" fill="none" stroke="#fff" stroke-width="1"><path d="M1 1l2.5 2.5L1 6M4.5 1 7 3.5 4.5 6"/></svg>
    </div>
    <div class="abs hero-photo" role="img" aria-label="Two loose brilliant-cut diamonds reflecting on black"></div>
  </section>

  <section class="abs arrivals">
    <div class="abs arrivals-label">NEW ARRIVALS</div>
    <div class="abs arrival-tile" style="left:163px;background:radial-gradient(circle at 50% 55%,var(--gold),#f3ead9 75%)" role="img" aria-label="Stacked gold and diamond bands"></div>
    <div class="abs arrival-tile" style="left:268px;background:radial-gradient(circle at 50% 50%,#b9c6d2,#f4f6f8 70%)" role="img" aria-label="Cushion halo diamond engagement ring"></div>
    <div class="abs arrival-tile" style="left:373px;background:radial-gradient(ellipse at 50% 60%,#cfd3d8,#fbfbfb 60%)" role="img" aria-label="Diamond flower drop earrings"></div>
    <div class="abs arrival-tile" style="left:478px;width:102px;background:radial-gradient(circle at 50% 55%,var(--rose),#f7ece6 75%)" role="img" aria-label="Rose gold beaded bands"></div>
  </section>

  <section class="abs jewelry-nav">
    <h2>Our Jewelry</h2>
    <a style="left:249px;top:27px">Rings</a>
    <a style="left:315px;top:27px">Bracelets</a>
    <a style="left:398px;top:27px">Estate</a>
    <a style="left:470px;top:27px">Men's</a>
    <a style="left:249px;top:52px">Earrings</a>
    <a style="left:315px;top:52px">Necklaces</a>
    <a style="left:398px;top:52px">Watches</a>
    <a style="left:470px;top:52px">Children's</a>
  </section>

  <section class="abs feature">
    <div class="abs feature-brand">Lunevelle</div>
    <div class="abs feature-line">Garden Wings</div>
    <div class="abs piece" style="left:220px;top:18px;width:115px;height:70px;background:radial-gradient(circle,var(--enamel-a) 0%,var(--enamel-b) 35%,transparent 68%)" role="img" aria-label="Enamel butterfly hoop earrings"></div>
    <div class="abs piece" style="left:365px;top:20px;width:125px;height:145px;background:radial-gradient(circle,var(--enamel-c) 0%,var(--enamel-a) 30%,var(--enamel-b) 45%,transparent 70%)" role="img" aria-label="Two enamel butterfly pendants"></div>
    <div class="abs piece" style="left:40px;top:120px;width:350px;height:190px;background:radial-gradient(ellipse,var(--enamel-b) 0%,var(--enamel-a) 30%,var(--enamel-c) 45%,transparent 70%)" role="img" aria-label="Two enamel butterfly bangles"></div>
    <div class="abs piece" style="left:440px;top:190px;width:75px;height:75px;background:radial-gradient(circle,var(--enamel-c) 0%,var(--enamel-a) 35%,var(--enamel-b) 50%,transparent 72%)" role="img" aria-label="Enamel butterfly dome ring"></div>
  </section>

  <footer class="abs site-footer">
    <div class="abs brand">BRILL'S</div>
    <div class="abs tagline">YOUR HOMETOWN JEWELER</div>
    <div class="abs foot-col" style="left:175px">
      <h3>LINK</h3>JEWELRY<br>SERVICES<br>ABOUT<br>CONTACT
    </div>
    <div class="abs foot-col" style="left:276px">
      <h3>CONTACT</h3>TEL (555) 014 2210<br>FAX (555) 014 2211<br>hello@brillsjewelers-example.com<br><span style="display:block;line-height:8px;padding-top:3px">48 Harbor Row, Palm<br>Vista, FL 00000</span>
    </div>
    <div class="abs foot-col" style="left:413px">
      <h3>OPENING HOURS</h3>MON - FRI &nbsp;&nbsp; 10 AM - 5:30 PM<br>SATURDAY &nbsp;11 AM - 5:00 PM
    </div>
    <div class="abs copyright">© Brill's Limited 2020. All Rights Reserved.</div>
  </footer>

  <div class="abs cookie-bar">
    <p class="abs cookie-text">Brill's uses cookies to improve your experience on this site and to share offers and updates suited to you. By continuing to browse our site, you consent to these cookies. You can opt out anytime here</p>
    <span class="abs cookie-link">Cookie Settings</span>
    <span class="abs cookie-accept">Accept All Cookies</span>
  </div>
</main>

<main class="mobile" aria-label="Brill's Jewelers home page, mobile">
  <div class="abs util-icons" style="left:100px;top:9px;gap:5px">
    <svg width="6" height="8" viewBox="0 0 7 9" fill="none" stroke="#fff" stroke-width="1"><circle cx="3.5" cy="2.5" r="2"/><path d="M0.5 8.5v-1a3 3 0 0 1 6 0v1z"/></svg>
    <span style="display:flex;gap:1px;align-items:center"><svg width="9" height="8" viewBox="0 0 10 9" fill="none" stroke="#fff" stroke-width="1"><path d="M5 8.2 1.2 4.5A2.2 2.2 0 0 1 5 1.9a2.2 2.2 0 0 1 3.8 2.6z"/></svg>0</span>
    <span style="display:flex;gap:1px;align-items:center"><svg width="9" height="8" viewBox="0 0 10 9" fill="none" stroke="#fff" stroke-width="1"><path d="M0.5 1h1.6l1.3 5h5l1-3.6H2.7"/><circle cx="4" cy="7.8" r=".7"/><circle cx="7.6" cy="7.8" r=".7"/></svg>0</span>
  </div>
  <div class="abs brand">BRILL'S</div>
  <div class="abs tagline">YOUR HOMETOWN JEWELER</div>
  <svg class="abs" style="left:136px;top:40px" width="10" height="8" viewBox="0 0 10 8" stroke="#fff" stroke-width="1"><path d="M0 1h10M0 4h10M0 7h10"/></svg>
  <h1 class="abs hero-title">Your Hometown Jeweler<br>Just Got a New Home</h1>
  <p class="abs hero-copy">You have trusted us for decades with your fine jewelry, custom designs, and repairs. Now come in and see what's in store!</p>
  <div class="abs hero-cta">Visit&nbsp; us today
    <svg width="8" height="7" viewBox="0 0 8 7" fill="none" stroke="#fff" stroke-width="1"><path d="M1 1l2.5 2.5L1 6M4.5 1 7 3.5 4.5 6"/></svg>
  </div>
  <div class="abs hero-photo" role="img" aria-label="Two loose brilliant-cut diamonds reflecting on black"></div>
</main>

</body>
</html>
```